Boutique custom software development company needs new business card

Our nearly 20 year old custom software development company would like to better include the fact that we are now providing Bitcoin services. These new services are B2B include education (how to acquire and securely hold Bitcoin) and integrating Bitcoin payments into existing ecommerce sites or other existing systems. Please keep the card clean and simple. Attached is our current design and some other files. vexalon.example

Target Market(s)

businesses owners interested in long term relationship

Industry/Entity Type

Custom software development and Bitcoin

Contact Information for Business Card

Marcus Ellwood, marcus@vexalon.example, vexalon.example, (888) 555-VEXAL

Font styles to use
Other font styles liked:
• monospace

Requirements
Must have
• double-sided
Nice to have
• clean and simple
Should not have
• physical address

```html
<!DOCTYPE html>
<html lang="en">
<head>
<meta charset="utf-8">
<title>Vexalon business card</title>
<link href="https://fonts.googleapis.com/css2?family=Montserrat:wght@500;700;800&family=Lato:wght@400;700&display=swap" rel="stylesheet">
<style>
  :root {
    --backdrop: #cfd3d4;
    --paper: #f6f6f4;
    --brand-blue: #2c64b0;
    --brand-orange: #e8731c;
    --ink: #333333;
    --faint-blue: #c8d7ea;
    --on-blue: #f4f4f2;
    --card-shadow: 0 18px 40px rgba(0,0,0,0.18);
  }
  * { box-sizing: border-box; margin: 0; padding: 0; }
  html, body {
    width: 1200px; height: 905px; overflow: hidden;
    background: var(--backdrop);
  }
  .canvas {
    width: 1200px; height: 905px;
    display: flex; flex-direction: column; align-items: center; justify-content: center;
    gap: 56px;
  }
  .card {
    position: relative;
    width: 650px; height: 372px;
    box-shadow: var(--card-shadow);
    overflow: hidden;
  }
  /* front side */
  .card--front { background: var(--paper); }
  .front-brand {
    position: absolute; left: 70px; top: 40px;
  }
  .brand-name {
    display: flex; align-items: center; gap: 10px;
    font-family: "Montserrat", sans-serif; font-weight: 800;
    color: var(--brand-blue); font-size: 40px; letter-spacing: 1px; line-height: 1;
  }
  .brand-mark {
    width: 22px; height: 22px; background: var(--brand-orange);
  }
  .tagline {
    font-family: "Lato", sans-serif; font-weight: 400;
    color: var(--brand-blue); font-size: 15px; margin-top: 8px; letter-spacing: -0.2px;
  }
  .services {
    font-family: "Lato", sans-serif; font-weight: 700;
    color: var(--brand-orange); font-size: 13px; margin-top: 3px; letter-spacing: 0.2px;
  }
  .identity {
    position: absolute; left: 0; top: 156px;
    display: flex; gap: 22px;
  }
  .identity-bar { width: 20px; height: 40px; background: var(--brand-orange); }
  .person-name {
    font-family: "Montserrat", sans-serif; font-weight: 700;
    font-size: 24px; letter-spacing: 1px; text-transform: uppercase; line-height: 1;
  }
  .person-name .first { color: var(--brand-orange); }
  .person-name .last { color: var(--brand-blue); }
  .person-role {
    font-family: "Montserrat", sans-serif; font-weight: 500;
    font-size: 15px; color: var(--ink); margin-top: 6px;
  }
  .contact-list {
    position: absolute; left: 48px; top: 240px; list-style: none;
    font-family: "Montserrat", sans-serif; font-weight: 500; font-size: 15px; color: var(--ink);
  }
  .contact-list li { display: flex; align-items: center; gap: 9px; height: 27px; }
  .contact-list svg { width: 13px; height: 13px; fill: var(--brand-blue); flex: none; }
  .backdrop-square {
    position: absolute; right: 60px; bottom: 40px;
    width: 230px; height: 230px; background: var(--faint-blue);
  }
  /* back side */
  .card--back {
    background: var(--brand-blue);
    display: flex; align-items: center; justify-content: center;
  }
  .back-brand { text-align: left; }
  .card--back .brand-name { color: var(--on-blue); font-size: 76px; gap: 18px; }
  .card--back .brand-mark { width: 38px; height: 38px; }
  .card--back .tagline { color: var(--on-blue); font-size: 27px; margin-top: 10px; margin-left: 4px; }
  .card--back .services { color: var(--on-blue); font-size: 19px; font-weight: 400; margin-top: 6px; margin-left: 4px; opacity: 0.9; }
</style>
</head>
<body>
<main class="canvas">
  <section class="card card--front" aria-label="Card front">
    <div class="backdrop-square" aria-hidden="true"></div>
    <div class="front-brand">
      <div class="brand-name"><span class="brand-mark"></span>VEXALON</div>
      <p class="tagline">developer of custom applications</p>
      <p class="services">Bitcoin education &amp; payment integration</p>
    </div>
    <div class="identity">
      <span class="identity-bar"></span>
      <div>
        <p class="person-name"><span class="first">Marcus</span> <span class="last">Ellwood</span></p>
        <p class="person-role">Owner</p>
      </div>
    </div>
    <ul class="contact-list">
      <li><svg viewBox="0 0 16 16" aria-hidden="true"><path d="M3.6 1.2l2.2 2.9-1.3 1.6c.9 2 2.3 3.5 4.4 4.4l1.6-1.3 2.9 2.2-1.3 2.6C7.4 13.4 2.6 8.6 1 3z"/></svg>(888) 555-VEXAL</li>
      <li><svg viewBox="0 0 16 16" aria-hidden="true"><path d="M1 3h14v10H1z M1.8 3.8L8 9l6.2-5.2" stroke="#f6f6f4" stroke-width="1"/></svg>marcus@vexalon.example</li>
      <li><svg viewBox="0 0 16 16" aria-hidden="true"><circle cx="8" cy="8" r="7"/></svg>www.vexalon.example</li>
    </ul>
  </section>

  <section class="card card--back" aria-label="Card back">
    <div class="back-brand">
      <div class="brand-name"><span class="brand-mark"></span>VEXALON</div>
      <p class="tagline">developer of custom applications</p>
      <p class="services">Bitcoin education &amp; payment integration</p>
    </div>
  </section>
</main>
</body>
</html>
```